Book cover design for a collection of poetry - The Lanternfield

Book cover and back design need to be moody, nostalgic, reflective, ethereal. Melancholy and other worldly. Cover design should not be time specific to a period or place but if applicable should reflect British landscape. Book cover should be in tones of blue and must include the title and author (THE LANTERNFIELD BY CORWIN BLACKETT). We love the idea of rain, and looking out of a window. See attached designs. A world you are observing but not in.

Industry/Entity Type

Book Publisher

Font styles to use
Serif
Script

Colors
3176b5
3377b5
85acd3
eaf1f7
0792cd
33a6d7
86cae7
ecf7fb
86cfc6

Requirements
Must have
• The colour blue in it, must be melancholy and reflective.
Nice to have
• Rain in the cover.
Should not have
• Any bright colours.

```html
<!DOCTYPE html>
<html lang="en">
<head>
<meta charset="utf-8">
<title>The Lanternfield – Book Cover</title>
<link rel="stylesheet" href="https://fonts.googleapis.com/css2?family=Cinzel:wght@400;600;700&family=Cormorant+Garamond:wght@500;600&family=Montserrat:wght@400;500&display=swap">
<style>
  :root {
    --ink-dark: #2b2b2d;
    --ink-body: #3a4046;
    --white: #ffffff;
    --rule-dark: #55595e;
    --rain-light: #eaf1f7;
    --rain-mid: #85acd3;
    --rain-deep: #3176b5;
    --glass: #86cae7;
    --slate: #4a6073;
    --night: #2c3844;
  }
  * { margin: 0; padding: 0; box-sizing: border-box; }
  html, body { width: 1200px; height: 864px; overflow: hidden; background: #ffffff; }
  .cover { position: relative; width: 1200px; height: 864px; overflow: hidden; }

  .photo-back {
    position: absolute; left: 0; top: 0; width: 600px; height: 864px;
    background:
      radial-gradient(ellipse 260px 200px at 150px 420px, rgba(140,170,140,0.5), transparent 70%),
      radial-gradient(ellipse 300px 180px at 380px 520px, rgba(150,180,160,0.45), transparent 70%),
      linear-gradient(180deg, #f1f5f8 0%, #dce8ef 30%, #b9cfd6 55%, #c6d8df 75%, #a9c2cf 100%);
  }
  .photo-front {
    position: absolute; left: 600px; top: 0; width: 600px; height: 864px;
    background:
      linear-gradient(180deg, rgba(234,241,247,0.12) 0%, rgba(0,0,0,0) 40%, rgba(20,28,36,0.35) 100%),
      linear-gradient(90deg, #8fb3ca 0%, #7397b2 14%, #62839d 38%, #536f86 62%, #3f5366 84%, var(--night) 100%);
  }

  .back-title { position: absolute; left: 0; top: 52px; width: 580px; }
  .rule { position: absolute; height: 1px; background: var(--rule-dark); }
  .back-subtitle {
    position: absolute; left: 0; top: 188px; width: 580px; text-align: center;
    font-family: "Cinzel", serif; font-weight: 700; font-size: 17px; letter-spacing: 1.5px; color: var(--ink-dark);
  }
  .blurb {
    position: absolute; left: 59px; top: 240px; width: 462px;
    font-family: "Cormorant Garamond", serif; font-weight: 600; font-size: 13.5px;
    letter-spacing: 3.2px; line-height: 26px; text-transform: uppercase; color: var(--ink-body);
    text-align: justify;
  }
  .blurb p { text-indent: 16px; margin-bottom: 4px; }

  .author-photo { position: absolute; left: 64px; top: 648px; width: 88px; height: 100px; }
  .about { position: absolute; left: 163px; top: 645px; width: 356px; font-family: "Montserrat", sans-serif; color: var(--ink-dark); }
  .about h2 { font-size: 9px; font-weight: 500; letter-spacing: 0.3px; line-height: 12px; }
  .about-line { display: block; font-size: 8.6px; line-height: 14.7px; white-space: nowrap; }
  .about-line.full { text-align: justify; text-align-last: justify; }
  .code-box { position: absolute; left: 356px; top: 722px; width: 192px; height: 114px; background: var(--white); }

  .spine { position: absolute; left: 560px; top: 0; width: 64px; height: 864px; }

  .front-type { position: absolute; left: 624px; top: 0; width: 576px; height: 864px; }
  .front-subtitle {
    position: absolute; left: 0; top: 624px; width: 556px; text-align: center;
    font-family: "Cinzel", serif; font-weight: 600; font-size: 25px; letter-spacing: 2.5px; color: var(--white);
  }
  .front-author {
    position: absolute; left: 0; top: 776px; width: 556px; text-align: center;
    font-family: "Cinzel", serif; font-weight: 600; font-size: 29px; letter-spacing: 0.5px; color: var(--white);
  }
  .rule-light { position: absolute; height: 1px; background: rgba(255,255,255,0.75); }
</style>
</head>
<body>
<main class="cover">
  <div class="photo-back" role="img" aria-label="Rain-streaked window glass with a soft, blurred green garden beyond"></div>
  <div class="photo-front" role="img" aria-label="A child gazing out of a rain-covered window in cool blue light"></div>

  <!-- Back cover -->
  <svg class="back-title" width="580" height="130" viewBox="0 0 580 130">
    <text x="291" y="54" text-anchor="middle" font-family="Cinzel, serif" font-weight="600" font-size="60" fill="#2b2b2d">THE</text>
    <text x="291" y="108" text-anchor="middle" font-family="Cinzel, serif" font-weight="600" font-size="52" fill="#2b2b2d" textLength="330" lengthAdjust="spacingAndGlyphs">LANTERNFIELD</text>
  </svg>
  <div class="rule" style="left:211px; top:181px; width:160px;"></div>
  <div class="back-subtitle">A COLLECTION OF POETRY</div>
  <div class="rule" style="left:211px; top:213px; width:160px;"></div>

  <div class="blurb">
    <p>Told in two parts we first meet Charles – aged, crippled and left alone in his inherited marsh house – reflecting on his life and his marriage to beautiful Alice who we meet in part two. Alice is suicidal, manically depressed and struggling with life as a wife and mother. She meets, harbors and falls in love with a soldier during WWII and her world is changed forever.</p>
    <p>Moving through the 20th century, this life and the next, The Lanternfield interweaves grief, loss, the after-life, mental illness, and ultimately the true nature of love.</p>
  </div>

  <div class="rule" style="left:59px; top:626px; width:463px; background:rgba(255,255,255,0.85);"></div>

  <svg class="author-photo" width="88" height="100" viewBox="0 0 88 100">
    <rect x="0.5" y="0.5" width="87" height="99" fill="#e6e6e6" stroke="#8a8a8a"/>
    <line x1="0" y1="0" x2="88" y2="100" stroke="#6a6a6a" stroke-width="0.8"/>
    <line x1="88" y1="0" x2="0" y2="100" stroke="#6a6a6a" stroke-width="0.8"/>
  </svg>
  <div class="about">
    <h2>ABOUT THE AUTHOR</h2>
    <span class="about-line full">Maribel is a Love and Relationship strategist. As head coach for</span>
    <span class="about-line full">men at Tollan's House for Men, Head Sunday school teacher in</span>
    <span class="about-line full">her local church and current leader of a women's prayer and</span>
    <span class="about-line full">support ministry, she has gained a wealth of experience and</span>
    <span class="about-line">wisdom around spirituality, family</span>
    <span class="about-line">and relationships.</span>
  </div>
  <div class="code-box"></div>

  <!-- Spine -->
  <svg class="spine" width="64" height="864" viewBox="0 0 64 864">
    <g transform="translate(43 25) rotate(90)">
      <text x="0" y="0" font-family="Cinzel, serif" font-size="14" letter-spacing="1.5" fill="#2b2b2d">A COLLECTION</text>
    </g>
    <g transform="translate(26 25) rotate(90)">
      <text x="10" y="0" font-family="Cinzel, serif" font-size="14" letter-spacing="1.5" fill="#2b2b2d">OF POETRY</text>
    </g>
    <g transform="translate(18 240) rotate(90)">
      <text x="0" y="0" font-family="Cinzel, serif" font-weight="600" font-size="36" fill="#ffffff" textLength="366" lengthAdjust="spacingAndGlyphs">THE LANTERNFIELD</text>
    </g>
    <g transform="translate(26 642) rotate(90)">
      <text x="0" y="0" font-family="Cinzel, serif" font-size="14" letter-spacing="1.5" fill="#ffffff" textLength="180">BY CORWIN BLACKETT</text>
    </g>
  </svg>

  <!-- Front cover -->
  <div class="front-type">
    <svg width="576" height="220" viewBox="0 0 576 220" style="position:absolute; left:0; top:0;">
      <defs>
        <filter id="title-shadow" x="-10%" y="-10%" width="120%" height="130%">
          <feDropShadow dx="2" dy="3" stdDeviation="2" flood-color="#000" flood-opacity="0.45"/>
        </filter>
      </defs>
      <text x="278" y="126" text-anchor="middle" font-family="Cinzel, serif" font-weight="600" font-size="124" fill="#ffffff" filter="url(#title-shadow)">THE</text>
      <text x="278" y="196" text-anchor="middle" font-family="Cinzel, serif" font-weight="600" font-size="66" fill="#ffffff" filter="url(#title-shadow)" textLength="512" lengthAdjust="spacingAndGlyphs">LANTERNFIELD</text>
    </svg>
    <div class="rule-light" style="left:144px; top:603px; width:267px;"></div>
    <div class="front-subtitle">A COLLECTION OF POETRY</div>
    <div class="rule-light" style="left:144px; top:673px; width:267px;"></div>
    <div class="front-author">BY CORWIN BLACKETT</div>
  </div>
</main>
</body>
</html>
```